Beekeeping company in need of a new attractive, simple website

We need a simple website for our Company 'Ridgecrest Apiary LLC' that will feature a couple different products that we offer (2019 NUCS & 2019 Queens) with the ability for customers to place orders for those products. Products will be for pickup only on specific dates so no shipping is required but will need dropdown menus to select which dates with limited quantities each date. Payments can be made through Coinvane, Plimo, and Tallyo. Need the to ability to add and remove products from view on the site while maintaining information. Would like the ability to build a mailing list of potential customers and also connect visitors to our social media sites.
Target Market(s)
Beekeepers,
Colors
Designer to choose colors to be used in the design.
Look and feel

```html
<!DOCTYPE html>
<html lang="en">
<head>
<meta charset="utf-8">
<title>Ridgecrest Apiary LLC</title>
<link rel="stylesheet" href="https://fonts.googleapis.com/css2?family=Anton&family=Montserrat:wght@400;500;600;700&family=Quicksand:wght@500&display=swap">
<style>
:root{
  --ink:#1c1b1a;
  --dark-brown:#2a1a10;
  --honey:#f0a818;
  --honey-deep:#e6960c;
  --cream:#fdeab8;
  --sand:#e3bd82;
  --paper:#f3eee6;
  --soft:#fdfbf5;
  --grey:#8a8a8a;
  --line:#ececec;
  --white:#ffffff;
}
*{box-sizing:border-box;margin:0;padding:0}
html,body{width:1200px;height:2811px;overflow:hidden}
body{position:relative;background:var(--white);font-family:"Montserrat",sans-serif;color:var(--ink)}
.abs{position:absolute}

/* header */
.site-header{left:0;top:0;width:1200px;height:128px;background:var(--ink)}
.brand{left:103px;top:38px;display:flex;align-items:center;gap:14px}
.brand-dot{width:46px;height:46px;border-radius:50%;background:var(--honey)}
.brand-name{font-weight:700;font-size:24px;line-height:28px;color:var(--honey);letter-spacing:1px;text-transform:uppercase}
.main-nav{top:58px;left:0;width:1200px}
.main-nav a{position:absolute;font-size:14px;font-weight:500;color:var(--honey);text-decoration:none;white-space:nowrap}
.main-nav a.active{color:var(--white)}

/* hero */
.hero{left:0;top:128px;width:1200px;height:528px;background:var(--cream)}
.hero-frame{left:163px;top:203px;width:878px;height:378px;background:var(--white);padding:9px}
.hero-photo{width:100%;height:100%;background:linear-gradient(135deg,#6b4a22 0%,#a87a3c 40%,#d7b07a 65%,#5a3c1c 100%)}
.hero-caption{left:163px;top:472px;width:878px;text-align:center;font-family:"Anton",sans-serif;font-size:44px;color:#f5c000;letter-spacing:.5px}
.hero-arrow{width:44px;height:44px;border-radius:50%;background:#3a3a3a;top:368px}
.hero-arrow svg{display:block;margin:14px auto}
.hero-dots{top:601px;left:576px;display:flex;gap:4px}
.hero-dots span{width:14px;height:14px;border-radius:50%;border:2px solid var(--honey-deep);background:var(--white)}
.hero-dots span.on{background:var(--honey-deep)}

/* products */
.section-title{font-weight:700;font-size:28px;color:var(--ink)}
.products-icon{left:98px;top:736px;width:40px;height:40px;border-radius:6px;background:#b8b8b8}
.product-card{top:799px;width:244px;height:304px;border:1px solid var(--line);background:var(--white)}
.product-photo{width:100%;height:204px}
.price-badge{position:absolute;right:12px;top:0;width:42px;height:44px;background:var(--honey);color:var(--white);font-size:13px;font-weight:600;text-align:center;line-height:40px;clip-path:polygon(0 0,100% 0,100% 100%,50% 84%,0 100%)}
.product-name{text-align:center;font-size:16px;font-weight:500;color:var(--dark-brown);margin-top:25px}
.buy-btn{display:block;width:98px;height:31px;margin:12px auto 0;background:var(--ink);color:var(--white);font-size:12px;font-weight:500;text-align:center;line-height:31px;text-decoration:none}

/* newsletter */
.newsletter{left:0;top:1209px;width:1200px;height:132px;background:var(--sand)}
.newsletter-icon{left:98px;top:1240px;width:62px;height:58px;background:#9c7a55;clip-path:polygon(25% 0,100% 10%,88% 80%,30% 100%,0 45%)}
.newsletter-title{left:169px;top:1250px;font-weight:700;font-size:28px;color:var(--dark-brown)}
.newsletter-input{left:399px;top:1251px;width:497px;height:43px;background:var(--white)}
.newsletter-btn{left:896px;top:1251px;width:135px;height:43px;background:var(--ink);color:var(--white);font-size:14px;font-weight:600;text-align:center;line-height:43px}

/* features */
.features{left:203px;top:1425px;width:800px;height:236px;background:var(--soft)}
.feature{top:1444px;width:240px;text-align:center}
.feature-art{width:90px;height:90px;margin:0 auto;border-radius:50%;background:#bcbcbc}
.feature-title{font-family:"Quicksand",sans-serif;font-weight:500;font-size:21px;color:var(--ink);margin-top:24px}
.feature-text{font-size:10.5px;line-height:15px;color:var(--grey);margin:8px auto 0;width:150px}
.operator{top:1476px;font-size:26px;font-weight:600;color:var(--ink)}

/* query */
.query{left:0;top:1719px;width:1200px;height:644px;background:radial-gradient(ellipse at 60% 40%,#5a3e22 0%,#3a2816 50%,#1e150c 100%)}
.query-kicker{left:0;top:1768px;width:1200px;text-align:center;font-size:14px;font-weight:600;color:var(--honey)}
.query-title{left:0;top:1788px;width:1200px;text-align:center;font-size:30px;font-weight:600;color:var(--white)}
.field{background:var(--white);font-size:12px;color:#333;padding-left:18px;line-height:38px}
.field.tall{line-height:normal;padding-top:16px}
.query-btn{left:246px;top:2216px;width:712px;height:42px;background:var(--cream);font-size:15px;font-weight:500;letter-spacing:1.5px;text-align:center;line-height:42px;color:var(--ink)}

/* footer */
.site-footer{left:0;top:2363px;width:1200px;height:393px;background:var(--paper)}
.footer-brand{left:90px;top:2404px;font-weight:700;font-size:30px;line-height:38px;color:var(--dark-brown);text-transform:uppercase;letter-spacing:1px}
.footer-about{left:88px;top:2508px;width:290px;font-size:12px;line-height:21px;color:#444}
.follow{left:95px;top:2596px;font-size:13px;font-weight:600}
.social{top:2629px;width:34px;height:34px;border-radius:50%;background:var(--honey)}
.footer-col h4{font-size:13px;font-weight:600;margin-bottom:18px}
.footer-col li{list-style:none;font-size:12px;line-height:32px;color:#333}
.bottom-bar{left:0;top:2756px;width:1200px;height:55px;background:var(--dark-brown);color:var(--white);font-size:12px;text-align:center;line-height:55px}
</style>
</head>
<body>

<header class="abs site-header">
  <div class="abs brand"><span class="brand-dot"></span><span class="brand-name">Ridgecrest<br>Apiary LLC</span></div>
  <nav class="abs main-nav">
    <a class="active" style="left:606px">Home</a>
    <a style="left:686px">About Us</a>
    <a style="left:793px">Products</a>
    <a style="left:896px">Query</a>
    <a style="left:981px">Shop</a>
    <a style="left:1056px">Contact</a>
  </nav>
</header>

<section class="abs hero">
</section>
<div class="abs hero-frame"><div class="hero-photo" role="img" aria-label="Photo of honey bees crawling over a wooden hive frame"></div></div>
<div class="abs hero-arrow" style="left:162px"><svg width="14" height="16" viewBox="0 0 14 16"><path d="M10 2 4 8l6 6" fill="none" stroke="#f0a818" stroke-width="3"/></svg></div>
<div class="abs hero-arrow" style="left:996px"><svg width="14" height="16" viewBox="0 0 14 16"><path d="M4 2l6 6-6 6" fill="none" stroke="#f0a818" stroke-width="3"/></svg></div>
<h1 class="abs hero-caption">Best Quality Queen Bees and NUCS provider</h1>
<div class="abs hero-dots"><span class="on"></span><span></span><span></span></div>

<div class="abs products-icon" role="img" aria-label="Honeycomb icon"></div>
<h2 class="abs section-title" style="left:169px;top:736px">Products</h2>

<article class="abs product-card" style="left:88px">
  <div class="product-photo" role="img" aria-label="Photo of a single queen bee" style="background:linear-gradient(135deg,#eeeeee,#e2e2e2)"></div>
  <span class="price-badge">$45</span>
  <p class="product-name">2019 Queen</p><a class="buy-btn">Buy Now</a>
</article>
<article class="abs product-card" style="left:349px">
  <div class="product-photo" role="img" aria-label="Photo of bees on a nucleus hive frame" style="background:linear-gradient(135deg,#4a3520,#8a6a40,#3a2a18)"></div>
  <span class="price-badge">$45</span>
  <p class="product-name">2019 NUCS</p><a class="buy-btn">Buy Now</a>
</article>
<article class="abs product-card" style="left:608px">
  <div class="product-photo" role="img" aria-label="Photo of a marked queen on comb cells" style="background:linear-gradient(135deg,#d79a3a,#b07028,#e0b060)"></div>
  <span class="price-badge">$45</span>
  <p class="product-name">2019 NUCS</p><a class="buy-btn">Buy Now</a>
</article>
<article class="abs product-card" style="left:866px">
  <div class="product-photo" role="img" aria-label="Photo of worker bees around a marked queen" style="background:linear-gradient(135deg,#3a2a1a,#9a6a30,#2a1e12)"></div>
  <span class="price-badge">$45</span>
  <p class="product-name">2019 Queen</p><a class="buy-btn">Buy Now</a>
</article>

<section class="abs newsletter"></section>
<div class="abs newsletter-icon" role="img" aria-label="Envelope icon"></div>
<h2 class="abs newsletter-title">Newsletter</h2>
<div class="abs newsletter-input"></div>
<div class="abs newsletter-btn">SUBSCRIBE</div>

<section class="abs features"></section>
<div class="abs feature" style="left:193px">
  <div class="feature-art" role="img" aria-label="Illustration of a bee"></div>
  <h3 class="feature-title">Duis autemve</h3>
  <p class="feature-text">Nam liber tempor cum soluta nobis eleifend option congue nihil imperdiet</p>
</div>
<div class="abs operator" style="left:446px">+</div>
<div class="abs feature" style="left:474px">
  <div class="feature-art" role="img" aria-label="Illustration of a beehive"></div>
  <h3 class="feature-title">Eodem modot</h3>
  <p class="feature-text">Nam liber tempor cum soluta nobis eleifend option congue nihil imperdiet</p>
</div>
<div class="abs operator" style="left:727px">=</div>
<div class="abs feature" style="left:756px">
  <div class="feature-art" role="img" aria-label="Illustration of honeycomb"></div>
  <h3 class="feature-title">Ut wisi enim adm</h3>
  <p class="feature-text">Nam liber tempor cum soluta nobis eleifend option congue nihil imperdiet</p>
</div>

<section class="abs query" role="img" aria-label="Dark photo of hands holding a frame covered in bees"></section>
<p class="abs query-kicker">Any Question</p>
<h2 class="abs query-title">Send your Query</h2>
<div class="abs field" style="left:246px;top:1879px;width:348px;height:38px">Your Name</div>
<div class="abs field" style="left:609px;top:1879px;width:349px;height:38px">Your Email</div>
<div class="abs field" style="left:246px;top:1944px;width:230px;height:38px">Product</div>
<div class="abs field" style="left:488px;top:1944px;width:230px;height:38px">Date</div>
<div class="abs field" style="left:728px;top:1944px;width:230px;height:38px">Quantity</div>
<div class="abs field" style="left:246px;top:2010px;width:712px;height:38px">Subject</div>
<div class="abs field tall" style="left:246px;top:2074px;width:712px;height:116px">Write your message here</div>
<div class="abs query-btn">SEND YOUR QUERY</div>

<footer class="abs site-footer"></footer>
<div class="abs footer-brand">Ridgecrest<br>Apiary LLC</div>
<p class="abs footer-about">Duis autem vel eum iriure dolor in hendrerit in vulputate velit esse molestie consequat, vel illum dolore eu feugiat nulla facilisis.</p>
<p class="abs follow">Follow Us</p>
<span class="abs social" style="left:90px" role="img" aria-label="Social link"></span>
<span class="abs social" style="left:126px" role="img" aria-label="Social link"></span>
<span class="abs social" style="left:161px" role="img" aria-label="Social link"></span>
<span class="abs social" style="left:197px" role="img" aria-label="Social link"></span>

<div class="abs footer-col" style="left:441px;top:2466px">
  <h4>Opening Hours</h4>
  <ul><li>Mon – Fri: 8AM – 10PM</li><li>Sat: 9AM-8PM</li><li>Sun: Closed</li></ul>
</div>
<div class="abs footer-col" style="left:694px;top:2462px">
  <h4>Information</h4>
  <ul><li>About Us</li><li>Delivery Information</li><li>Privacy Policy</li><li>Terms &amp; Conditions</li><li>Customer Service</li><li>Return Policy</li></ul>
</div>
<div class="abs footer-col" style="left:930px;top:2457px">
  <h4>Account Info</h4>
  <ul style="margin-left:6px"><li>My account</li><li>Wishlist</li><li>Newsletter</li><li>Order History</li><li>International Orders</li><li>Contact</li></ul>
</div>

<div class="abs bottom-bar">© All Rights Reserved - 2019</div>

</body>
</html>
```